VFX Company Business Card Design Project

The Pixel Harbor is a decentralized Visual Effects Studio servicing the television and feature film industries.
Project Brief:
Take our logo that was previously designed on Sketch Forum and make a double sided business card.
Requirements:
- Card MUST be double sided.
- Front of card MUST have the yellow part of our logo against the dark grey background.
- Back of card is completely up to the designer.
- Back of card must include the complete company logo.
Please follow these File Preparation guidelines:
http://printmarlow.example/infopage?file=filetype_en&s=PrintMarlow_new&lang=en
Industry/Entity Type
Business
Look and feel
Each slider illustrates characteristics of the customer's brand and the style your logo design should communicate.

```html
<!DOCTYPE html>
<html lang="en">
<head>
<meta charset="utf-8">
<title>The Pixel Harbor — Business Card</title>
<link href="https://fonts.googleapis.com/css2?family=Josefin+Sans:wght@300;400;600&display=swap" rel="stylesheet">
<style>
  :root {
    --page: #ffffff;
    --card-dark: #252525;
    --brand-yellow: #fec92a;
    --band-yellow: #fbc11f;
    --ink-grey: #44464a;
    --logo-grey: #5c6167;
    --paper-white: #ffffff;
  }
  * { margin: 0; padding: 0; box-sizing: border-box; }
  html, body {
    width: 1200px;
    height: 921px;
    overflow: hidden;
    background: var(--page);
    font-family: "Josefin Sans", sans-serif;
  }
  .canvas { position: relative; width: 1200px; height: 921px; }

  .card {
    position: absolute;
    width: 635px;
    height: 317px;
    overflow: hidden;
  }

  /* Front side */
  .card-front {
    left: 310px;
    top: 117px;
    background: var(--card-dark);
    display: flex;
    align-items: center;
    justify-content: center;
  }
  .front-wordmark {
    color: var(--brand-yellow);
    font-weight: 600;
    font-size: 54px;
    letter-spacing: 0.02em;
  }

  /* Back side */
  .card-back {
    left: 309px;
    top: 479px;
    background: var(--brand-yellow);
  }
  .back-band {
    position: absolute;
    left: 310px;
    top: 0;
    width: 26px;
    height: 100%;
    background: var(--band-yellow);
  }
  .company-block {
    position: absolute;
    right: 32px;
    top: 24px;
    text-align: right;
  }
  .company-name {
    color: var(--logo-grey);
    font-weight: 600;
    font-size: 33px;
    line-height: 1;
    letter-spacing: -0.01em;
  }
  .company-address {
    margin-top: 14px;
    color: var(--logo-grey);
    font-weight: 300;
    font-size: 15px;
    letter-spacing: -0.02em;
  }
  .person {
    position: absolute;
    left: 40px;
    top: 236px;
  }
  .person-name {
    color: var(--ink-grey);
    font-weight: 600;
    font-size: 26px;
    line-height: 1;
    letter-spacing: 0.01em;
  }
  .person-title {
    margin-top: 12px;
    color: var(--paper-white);
    font-weight: 400;
    font-size: 18px;
    letter-spacing: 0.36em;
  }
  .contact {
    position: absolute;
    left: 347px;
    top: 229px;
    list-style: none;
    color: var(--paper-white);
    font-weight: 400;
    font-size: 17px;
    line-height: 22px;
    letter-spacing: 0.13em;
  }
</style>
</head>
<body>
  <main class="canvas">
    <section class="card card-front" aria-label="Card front">
      <p class="front-wordmark">The Pixel Harbor</p>
    </section>

    <section class="card card-back" aria-label="Card back">
      <div class="back-band"></div>

      <div class="company-block">
        <p class="company-name">The Pixel Harbor</p>
        <p class="company-address">4120 Quarry Lane Oakdale, CA 95361</p>
      </div>

      <div class="person">
        <p class="person-name">MARCUS ELLERY</p>
        <p class="person-title">Creative Director</p>
      </div>

      <ul class="contact">
        <li>mellery@pixelharbor.example</li>
        <li>(555) 014-2290</li>
        <li>PIXELHARBOR.EXAMPLE</li>
      </ul>
    </section>
  </main>
</body>
</html>
```